Business card for a shipping supplies business

Needing a business card design. Please see the logo. The logo with the white font should be used if there is a dark background.

We are looking for the following info on the card. Please see the sample info. We will need the info to be changed with a few different employee names and info but all will use the same template.

Business Name: The Crate Heron
Employee Name : Marcus Delaney
Position: Account Manager
Address: 4827 W. Ridge 418 S.
Fort Worth, TX 73948
email: Marcus@thecrateheron.example
telephone: 855-619-2740 x 207
website: www.getparcelkits.example

Target Market(s)

Businesses who ship products for online sales

Industry/Entity Type

Cardboard

Contact Information for Business Card

Name, title, address, website, logo, telephone number

Font styles to use
Sans Serif

Colors
EE7325
F08F49
F5BC92
FAE3D3
FDF4ED

Requirements
Must have
• Logo on back of card. Clean look, just logo, website address

```html
<!DOCTYPE html>
<html lang="en">
<head>
<meta charset="UTF-8">
<title>The Crate Heron — Business Card</title>
<link href="https://fonts.googleapis.com/css2?family=Montserrat:wght@400;500;600;700;800&display=swap" rel="stylesheet">
<style>
  :root {
    --orange: #EE7325;
    --orange-mid: #F08F49;
    --orange-soft: #F5BC92;
    --peach: #FAE3D3;
    --cream: #FDF4ED;
    --ink: #1f1f1f;
    --card-dark: #1b1b1b;
    --text: #333333;
    --muted: #6b6b6b;
    --stage: #eeeeee;
  }
  * { box-sizing: border-box; margin: 0; padding: 0; }
  html, body { width: 900px; height: 1200px; overflow: hidden; }
  body {
    background: var(--stage);
    font-family: "Montserrat", sans-serif;
    display: flex;
    flex-direction: column;
    align-items: center;
    justify-content: center;
    gap: 90px;
  }
  .card {
    width: 760px;
    height: 434px;
    border-radius: 6px;
    box-shadow: 0 10px 30px rgba(0,0,0,0.12);
    position: relative;
    overflow: hidden;
  }

  /* Back of card */
  .card-back {
    background: var(--card-dark);
    display: flex;
    align-items: center;
    justify-content: center;
  }
  .brand {
    display: flex;
    align-items: center;
    gap: 22px;
  }
  .brand-mark {
    width: 78px;
    height: 78px;
    background: var(--orange);
    border-radius: 8px;
  }
  .brand-name {
    font-weight: 800;
    font-size: 52px;
    letter-spacing: 1px;
    color: #ffffff;
  }

  /* Front of card */
  .card-front {
    background: #ffffff;
    display: flex;
    align-items: center;
    padding: 0 56px 0 50px;
  }
  .front-brand {
    width: 250px;
    display: flex;
    flex-direction: column;
    align-items: flex-start;
    gap: 16px;
  }
  .front-brand .brand-mark { width: 96px; height: 96px; }
  .front-brand .brand-name {
    color: var(--ink);
    font-size: 34px;
  }
  .details {
    flex: 1;
    padding-left: 30px;
  }
  .company {
    color: var(--orange);
    font-weight: 800;
    font-size: 15px;
    letter-spacing: 1px;
    text-transform: uppercase;
  }
  .tagline {
    color: var(--ink);
    font-weight: 700;
    font-size: 10px;
    letter-spacing: 1.5px;
    text-transform: uppercase;
    margin-top: 2px;
  }
  .person-name {
    margin-top: 26px;
    font-weight: 600;
    font-size: 30px;
    color: var(--ink);
  }
  .person-title {
    font-size: 14px;
    color: var(--muted);
    margin-top: 2px;
  }
  .address {
    margin-top: 22px;
    font-size: 13px;
    color: var(--text);
    line-height: 1.55;
  }
  .contacts {
    margin-top: 22px;
    display: grid;
    grid-template-columns: 1fr 1fr;
    row-gap: 12px;
    column-gap: 14px;
  }
  .contact {
    display: flex;
    align-items: center;
    gap: 8px;
    font-size: 11.5px;
    color: var(--text);
    white-space: nowrap;
  }
  .contact-icon {
    width: 18px;
    height: 18px;
    flex: none;
  }
</style>
</head>
<body>

  <section class="card card-back">
    <div class="brand">
      <span class="brand-mark"></span>
      <span class="brand-name">CRATE HERON</span>
    </div>
  </section>

  <section class="card card-front">
    <div class="front-brand">
      <span class="brand-mark"></span>
      <span class="brand-name">CRATE HERON</span>
    </div>

    <div class="details">
      <p class="company">The Crate Heron</p>
      <p class="tagline">Ship Products</p>

      <p class="person-name">Marcus Delaney</p>
      <p class="person-title">Account Manager</p>

      <p class="address">4827 W. Ridge 418 S. Fort Worth,<br>TX 73948</p>

      <div class="contacts">
        <div class="contact">
          <svg class="contact-icon" viewBox="0 0 18 18"><circle cx="9" cy="9" r="9" fill="var(--orange)"/><path d="M6.2 4.8l1.6 0 .7 2-1 .8a6 6 0 0 0 2.9 2.9l.8-1 2 .7v1.6a1 1 0 0 1-1.1 1A8 8 0 0 1 5.2 5.9a1 1 0 0 1 1-1.1z" fill="#fff"/></svg>
          <span>855-619-2740 x 207</span>
        </div>
        <div class="contact">
          <svg class="contact-icon" viewBox="0 0 18 18"><circle cx="9" cy="9" r="9" fill="var(--orange)"/><rect x="6" y="4.5" width="6" height="3" fill="#fff"/><rect x="4.5" y="7.5" width="9" height="4" rx="1" fill="#fff"/><rect x="6" y="10.5" width="6" height="3" fill="#fff" stroke="var(--orange)" stroke-width=".6"/></svg>
          <span>855-619-2740</span>
        </div>
        <div class="contact">
          <svg class="contact-icon" viewBox="0 0 18 18"><circle cx="9" cy="9" r="9" fill="var(--orange)"/><rect x="4.5" y="5.8" width="9" height="6.4" rx="1" fill="#fff"/><path d="M4.8 6.2L9 9.4l4.2-3.2" fill="none" stroke="var(--orange)" stroke-width="1"/></svg>
          <span>Marcus@thecrateheron.example</span>
        </div>
        <div class="contact">
          <svg class="contact-icon" viewBox="0 0 18 18"><circle cx="9" cy="9" r="9" fill="var(--orange)"/><circle cx="9" cy="9" r="4.6" fill="none" stroke="#fff" stroke-width="1"/><ellipse cx="9" cy="9" rx="2" ry="4.6" fill="none" stroke="#fff" stroke-width="1"/><path d="M4.4 9h9.2" stroke="#fff" stroke-width="1"/></svg>
          <span>www.getparcelkits.example</span>
        </div>
      </div>
    </div>
  </section>

</body>
</html>
```